INTRODUCING - BRINDLE MOTOR CENTRE

WE WOULD LIKE TO TIDY UP OUR INTRODUCTION TO OUR COMPANY
WE NEED THE WORDING TO BE SIMILAR WITH our web page
https://brindlemotorcentre.example.nz/services/

this needs to be more concise with pictures added THAT TIE IN WITH EXPLAINATIONS

```html
<!DOCTYPE html>
<html lang="en">
<head>
<meta charset="utf-8">
<title>Brindle Motor Centre – Introduction Flyer</title>
<link href="https://fonts.googleapis.com/css2?family=Montserrat:ital,wght@0,400;0,500;0,600;0,700;1,700&display=swap" rel="stylesheet">
<style>
:root{
  --yellow:#f7d917;
  --charcoal:#232323;
  --ink:#1f1f1f;
  --paper:#ffffff;
  --paper-shade:#dcdcdc;
  --stage:#e6e6e6;
  --rule:#e3c514;
}
*{box-sizing:border-box;margin:0;padding:0}
html,body{width:1050px;height:1200px;overflow:hidden;background:var(--stage)}
body{font-family:"Montserrat",sans-serif;color:var(--ink);position:relative}
.page{position:absolute;top:239px;width:510px;height:722px;background:radial-gradient(ellipse at 45% 40%,var(--paper) 55%,var(--paper-shade) 100%);overflow:hidden;box-shadow:0 4px 14px rgba(0,0,0,.25)}
.page--front{left:10px}
.page--back{left:530px}
.abs{position:absolute}
.shapes{position:absolute;left:0;top:0}
p,li{font-size:7.8px;line-height:9.8px}
h2{font-weight:700;font-size:12.5px}
h3{font-weight:700;font-size:10px}
ul{list-style:none}
li::before{content:"• ";}
.bottom-bands{position:absolute;left:0;bottom:0;width:100%;height:10px;background:linear-gradient(to bottom,#9a9a9a 0 3px,transparent 3px 5px,var(--charcoal) 5px 100%)}
/* front */
.brand-box{left:202px;top:46px;width:106px;height:76px;background:var(--yellow);display:flex;align-items:center;justify-content:center;text-align:center}
.brand-name{font-weight:700;font-size:10.5px;line-height:13px;color:var(--charcoal);letter-spacing:.5px}
.cables{left:22px;top:238px;width:262px}
.cables p{margin-top:8px}
.cable-list{left:22px;top:424px;width:270px;display:grid;grid-template-columns:120px 1fr;row-gap:3.6px}
.cable-list li{font-size:7.9px}
.photo-frame{background:#f4f4f4;box-shadow:0 1px 3px rgba(0,0,0,.18)}
.cable-frame{left:32px;top:545px;width:254px;height:156px}
.photo{position:absolute;left:7px;top:5px;right:7px;bottom:5px}
.photo-cable{background:linear-gradient(100deg,#141414,#4b4b4b 35%,#1c1c1c 60%,#555 85%,#202020)}
.welcome{left:313px;top:214px;width:197px;text-align:center;color:#fff}
.welcome .kicker{color:var(--yellow);font-weight:700;font-size:8px}
.welcome .title{color:var(--yellow);font-weight:400;font-size:11.2px;margin-top:2px}
.welcome p{color:#fff;margin:10px 12px 0}
.contact{left:302px;top:615px;width:208px;text-align:center}
.contact .head{font-size:10.5px;text-decoration:underline;color:var(--charcoal)}
.contact .addr{font-weight:700;font-size:9.4px;line-height:11px;margin-top:8px}
.contact .phone{font-size:8px;margin-top:6px}
.contact .phone b{font-size:12.5px}
.contact .email{font-size:7.6px;margin-top:5px}
.contact .email b{font-weight:700}
/* back */
.brake-frame{left:19px;top:25px;width:168px;height:123px}
.photo-brake{background:radial-gradient(circle at 40% 55%,#c7c7c7,#8d8d8d 40%,#f2f2f2 72%)}
.brakes{left:210px;top:25px;width:284px}
.brakes p{margin-top:4px}
.brakes p + p{margin-top:8px}
.brake-list{left:34px;top:160px;width:460px;display:grid;grid-template-columns:219px 1fr;row-gap:3.6px}
.brake-list li.wide{grid-column:1 / 3}
.rule{height:1.2px;background:var(--rule);left:25px;width:464px}
.parts{left:25px;top:258px;width:280px}
.parts p{margin-top:4px}
.parts p + p{margin-top:8px}
.shelf-frame{left:314px;top:256px;width:171px;height:128px}
.photo-shelf{background:linear-gradient(90deg,#6b4a2c,#b08a5e 25%,#e8e4d8 48%,#a57c4f 72%,#5d4028)}
.parts-head{left:25px;top:393px;font-weight:700;font-style:italic;font-size:8.4px}
.parts-list{left:34px;top:408px;width:460px;display:grid;grid-template-columns:156px 124px 1fr;row-gap:3.6px}
.hose-frame{left:19px;top:524px;width:168px;height:127px}
.photo-hose{background:linear-gradient(135deg,#6f8da6,#3e5a74 45%,#b9c2c8 75%,#4b6177)}
.hoses{left:194px;top:525px;width:296px}
.hoses p{margin-top:4px;text-align:justify}
.hoses h3 + p{margin-top:5px}
.hoses h3{margin-top:9px}
.hoses h3:first-child{margin-top:0}
</style>
</head>
<body>

<section class="page page--front" aria-label="Front page">
  <svg class="shapes" width="510" height="722" viewBox="0 0 510 722">
    <g role="img" aria-label="Photograph of dark mountain ridges at dusk">
      <defs>
        <linearGradient id="mountains" x1="0" y1="0" x2="0.3" y2="1">
          <stop offset="0" stop-color="#2a2a27"/>
          <stop offset="0.6" stop-color="#46453f"/>
          <stop offset="1" stop-color="#25241f"/>
        </linearGradient>
      </defs>
      <polygon points="0,0 510,0 510,160 150,236 0,182" fill="url(#mountains)"/>
    </g>
    <polygon points="0,186 150,240 510,164 510,170 150,250 0,194" fill="var(--yellow)"/>
    <polygon points="313,206 510,166 510,722 313,722" fill="var(--charcoal)"/>
    <polygon points="302,585 510,623 510,722 302,722" fill="var(--yellow)"/>
  </svg>

  <div class="abs brand-box"><span class="brand-name">BRINDLE<br>MOTOR CENTRE</span></div>

  <div class="abs cables">
    <h2>Cables</h2>
    <p>At Brindle Motor Centre we design, manufacture &amp; distribute specially engineered cables for a wide range of customers including marine, agriculture, lawn care, trucking, heavy lifting &amp; recreational vehicle. We utilise the Linkwire system in producing our push/pull cables and these cables are used throughout the world with recongised brands such as Kelvorn, Brastow and Alderwing.</p>
    <p>We strive to add value by listening to our customers, understanding their needs and working to provide innovative solutions. As our cables are all made on site so we are able to offer our customers a quick turnaround time. Our reputation as a supplier of premium products has been earned for over 20 years in New Zealand.</p>
  </div>

  <ul class="abs cable-list">
    <li>Hand Brake</li><li>Clutch Cable</li>
    <li>Motor Cycle</li><li>Marine</li>
    <li>Throttle</li><li>Gear Shifter Cables</li>
    <li>Transmission</li><li>Excavator</li>
    <li>Push Pull</li><li>Agricultural</li>
    <li>Marine</li><li>Speedo Cables</li>
    <li>Remote Cable Controls</li>
  </ul>

  <div class="abs photo-frame cable-frame">
    <div class="photo photo-cable" role="img" aria-label="Close-up photograph of coiled black control cable"></div>
  </div>

  <div class="abs welcome">
    <div class="kicker">WELCOME</div>
    <div class="title">TO BRINDLE MOTOR CENTRE</div>
    <p>Whether your car is a late model or a classic, Brindle can repair or manufacture brake and clutch parts for you. Brindle Motor Centre is a Hamilton based company who are the specialists for hard to source cables, brake parts &amp; hoses – cars, motorbikes, trucks, agriculture &amp; industrial.</p>
    <p>Our RMC approved workshop can undertake all types of vehicle repairs. Our aim is to repair or manufacture parts with the quickest turnaround time possible.</p>
    <div class="title" style="margin-top:22px">A LITTLE ABOUT US</div>
    <p>Brindle Motor Centre is a Hamilton based company who are the specialists for hard to source cables, brake parts &amp; hoses – cars, motorbikes, trucks, agriculture &amp; industrial.</p>
    <p>Our RMC aproved workshop can undertake all types of vehicle repairs. Whether your vehicle is a late model a classic or a commercial Brindle can repair or manufacture parts for you.</p>
  </div>

  <div class="abs contact">
    <div class="head">CONTACT US</div>
    <div class="addr">18 Larchmont Rd, Eastfield,<br>Hamilton</div>
    <div class="phone">Phone: <b>0800 55 41 20</b></div>
    <div class="email">Email: <b>parts@brindlemotorcentre.example.nz</b></div>
  </div>

  <div class="bottom-bands"></div>
</section>

<section class="page page--back" aria-label="Back page">
  <div class="abs photo-frame brake-frame">
    <div class="photo photo-brake" role="img" aria-label="Photograph of a reconditioned brake caliper"></div>
  </div>

  <div class="abs brakes">
    <h2>BRAKES</h2>
    <p>Brindle Motor Centre specialise in the repair of all brake components including resleeving cylinders, boosters, calipers, proportioning valves &amp; brake linings. All our resleeving is carried out using seamless stainless steel. Brake caliper seals and pistons do require replacement overtime; if new pistons are unavailable these can also be resleeved in stainless steel.</p>
    <p>We also rebuild Brake boosters and porportioning valves, providing all parts are available and are also capable to have products relined in brake material. Brindle Motor Centre prides it selves in ensuring a quick turnaround for all of the above services.</p>
  </div>

  <ul class="abs brake-list">
    <li>Stainless Steel Resleeving</li><li>Brake Caliper Rebuilds</li>
    <li>Booster Reconditioning</li><li>Exchange Cylinders available</li>
    <li>Cost Effective saving time and money</li><li>Disc Caliper Pistons – Resleeved or Manufactured</li>
    <li class="wide">All types of cylinders, pistons, booster bodies can be resleeved or repaired</li>
    <li class="wide">Quick turn-a-round. Most cylinders received early morning will be processed and despatched same day<br>&nbsp;&nbsp;(subject to parts availablity)</li>
  </ul>

  <div class="abs rule" style="top:244px"></div>

  <div class="abs parts">
    <h2>Parts</h2>
    <p>Here at Brindle Motor Centre we hold an extensive range of specialised parts for all your brake requirements. We specialise in the “hard to get” parts. We can source components from overseas when needs require and are specialists in making and supplying components for brake pipes.</p>
    <p>Apart from our reconditioning program we have access to and extensive range of parts including hydraulic cylinders, shoes, drums, rotors, pads, repair kits, etc. We cater for vehicle from 1920’s to current models with that in mind with over 20 years in business we understand the needs and wants of our customers.</p>
  </div>

  <div class="abs photo-frame shelf-frame">
    <div class="photo photo-shelf" role="img" aria-label="Photograph of a warehouse aisle lined with shelves of boxed parts"></div>
  </div>

  <div class="abs parts-head">We have the following parts available:</div>
  <ul class="abs parts-list">
    <li>Flywheel Machining</li><li style="visibility:hidden">.</li><li>Commercial Wheel Cylinders</li>
    <li>Hydraulic Brake Kits and Seals</li><li style="visibility:hidden">.</li><li>Brake Boosters, Kits and Seals</li>
    <li>Brake Hoses</li><li>Disc Rotors</li><li>Disc Pads</li>
    <li>Brake Shoes</li><li>Brake Shoe Rebonding</li><li>Clutch Parts (new and reconditioned)</li>
    <li style="grid-column:1 / 3">Brake Piping (Coilwall tube, tube nuts etc)</li><li>Disc and Drum machining</li>
    <li>CV Joints</li><li style="grid-column:2 / 4">Brake Fluid (Super Heavy Duty, 500ml)</li>
    <li>Clearbrake Parts Cleaner</li>
  </ul>

  <div class="abs rule" style="top:510px"></div>

  <div class="abs photo-frame hose-frame">
    <div class="photo photo-hose" role="img" aria-label="Photograph of a technician's hands crimping a brake hose fitting in a press"></div>
  </div>

  <div class="abs hoses">
    <h3>Hoses</h3>
    <p>Brindle Motor Centre have been manufacturing brake hoses for more than 15 years. The hose and end fittings that we have in stock should enable us to supply brake hoses for up to 90% of the vehicles on the road today. Most brake hoses can be made while you wait.</p>
    <h3>Automotive Hoses</h3>
    <p>Brindle Motor Centre make on site, Power Steering hoses, Fuel hoses, etc., for any application needed on your vehicle.</p>
    <h3>Braided Hoses</h3>
    <p>To compliment our Brake and Automotive hoses, Brindle Motor Centre can offer to have your hoses made in Braid for greater endurance and better look. Brindle have a large range of hoses and fittings to make or supply to our customers needs.</p>
  </div>

  <div class="bottom-bands"></div>
</section>

</body>
</html>
```